Business Card Design

I need a good card to sell my talents in the music field and get my name known as a musician/Guitarist

Industry/Entity Type

Business

Contact Information for Business Card

Nathaniel Brisco Musician/Guitarist

```html
<!DOCTYPE html>
<html lang="en">
<head>
<meta charset="utf-8">
<title>Nathaniel Brisco – Business Card</title>
<link rel="stylesheet" href="https://fonts.googleapis.com/css2?family=Libre+Franklin:wght@700;800&family=Arimo:wght@400;700&display=swap">
<style>
  :root {
    --backdrop-light: #f4f4f5;
    --backdrop-dark: #c9cacc;
    --card-white: #f7f7f7;
    --card-edge: #e0343a;
    --brand-red: #e8313a;
    --soft-red: #ef5350;
    --peach: #f6a96c;
    --shade: #3a3a3a;
    --ink: #1d1d1d;
    --muted: #4a4a4a;
    --guitar-tone: #1f1f1f;
  }
  * { box-sizing: border-box; margin: 0; padding: 0; }
  html, body { width: 1200px; height: 969px; overflow: hidden; }
  body {
    position: relative;
    background: radial-gradient(ellipse at 50% 40%, var(--backdrop-light) 0%, var(--backdrop-dark) 100%);
    font-family: "Arimo", Arial, sans-serif;
  }
  .card {
    position: absolute;
    left: 220px;
    width: 760px;
    height: 434px;
    background: var(--card-white);
    border: 1.5px solid var(--card-edge);
    overflow: hidden;
    box-shadow: 0 10px 24px rgba(0,0,0,0.18);
  }
  .card--front { top: 30px; }
  .card--back { top: 505px; }
  .card__art { position: absolute; inset: 0; width: 100%; height: 100%; }
  .card__name {
    position: absolute;
    font-family: "Libre Franklin", Arial, sans-serif;
    font-weight: 800;
    color: var(--brand-red);
    text-transform: uppercase;
    letter-spacing: 0.2px;
    white-space: nowrap;
  }
  .card__role { position: absolute; color: var(--muted); white-space: nowrap; }

  .card--front .card__name { left: 44px; top: 170px; font-size: 30px; }
  .card--front .card__role { left: 260px; top: 208px; font-size: 13px; }
  .contact { position: absolute; left: 44px; top: 236px; color: var(--ink); font-weight: 700; }
  .contact__line { white-space: nowrap; }
  .contact__line--phone { font-size: 22px; line-height: 26px; letter-spacing: 0.5px; }
  .contact__line--web { font-size: 15px; line-height: 21px; }
  .contact__line--phone + .contact__line--web { margin-top: 4px; }

  .card--back .card__name { left: 56px; top: 190px; font-size: 38px; }
  .card--back .card__role { left: 150px; top: 238px; font-size: 24px; }
  .card__site {
    position: absolute; left: 56px; bottom: 24px;
    font-size: 14px; font-weight: 700; color: var(--ink);
  }
  .guitar-art {
    position: absolute; right: 80px; top: 24px;
    width: 210px; height: 370px;
    background: linear-gradient(180deg, var(--guitar-tone) 0%, #3b3b3b 100%);
    opacity: 0.85;
    border-radius: 60px 60px 90px 90px;
  }
</style>
</head>
<body>

<section class="card card--front">
  <svg class="card__art" viewBox="0 0 760 434" aria-hidden="true">
    <path d="M385 0 C470 40 540 150 760 240 L760 0 Z" fill="var(--brand-red)"/>
    <path d="M385 0 C430 60 480 130 580 190 C520 140 480 70 462 0 Z" fill="var(--shade)" opacity="0.85"/>
    <path d="M310 434 C370 300 470 205 620 195 C500 220 420 320 380 434 Z" fill="var(--peach)"/>
    <path d="M350 434 C410 300 520 215 760 205 L760 434 Z" fill="var(--soft-red)" opacity="0.92"/>
    <path d="M560 200 C640 230 700 240 760 240 L760 205 C690 205 620 200 560 200 Z" fill="var(--brand-red)" opacity="0.7"/>
  </svg>
  <h1 class="card__name">Nathaniel Brisco</h1>
  <p class="card__role">(Musician/Guitarist)</p>
  <div class="contact">
    <p class="contact__line contact__line--phone">Tel: 01632 960412</p>
    <p class="contact__line contact__line--phone">Mob: 07700900318</p>
    <p class="contact__line contact__line--web">Email : nathaniel@briscotone.net</p>
    <p class="contact__line contact__line--web">Website: www.nathanielbrisco.net</p>
  </div>
</section>

<section class="card card--back">
  <svg class="card__art" viewBox="0 0 760 434" aria-hidden="true">
    <path d="M300 0 C420 70 560 150 760 150 L760 0 Z" fill="var(--brand-red)"/>
    <path d="M380 60 C480 140 600 170 760 160 L760 150 C600 150 480 110 380 60 Z" fill="var(--shade)" opacity="0.25"/>
    <path d="M420 434 C450 300 510 200 620 160 C560 230 520 330 500 434 Z" fill="var(--peach)"/>
    <path d="M480 434 C510 300 580 200 760 150 L760 434 Z" fill="var(--soft-red)" opacity="0.92"/>
  </svg>
  <div class="guitar-art" role="img" aria-label="Black electric guitar silhouette"></div>
  <h2 class="card__name">Nathaniel Brisco</h2>
  <p class="card__role">(Musician/Guitarist)</p>
  <p class="card__site">www.nathanielbrisco.net</p>
</section>

</body>
</html>
```